Logo & Visitenkarte für Soziale Dienstleistungen, Beratung & Therapie
Zielgruppe
[frontside]
Konrad Wallmuth
Dipl. Sozialpädagoge (FH)
systemischer Einzel-, Paar- und Familientherapeut (VKTB)
Mobil: 0176 / 4 829 31 57
Mail: konrad-wallmuth@rundpost.de
'Soziale Dienstleistungen, Beratung & Therapie' [slogan]
[social services, counseling & therapy]
'systemische Beratung & Therapie,
ambulante Hilfen zur Erziehung, intensive Familienberatung, aufsuchende Familientherapie
soziale Projekte, Erwachsenenbildung, Lehraufträge' [business offers - backside of the card]
Zielgruppen [traget groups]:
Familien, Kinder- und Jugendliche, Einzelpersonen, Netzwerkpartner,
Institutionen, Ämter, Schulen, Kliniken, etc.

```html
<!DOCTYPE html>
<html lang="de">
<head>
<meta charset="utf-8">
<title>Konrad Wallmuth – Visitenkarte</title>
<link rel="stylesheet" href="https://fonts.googleapis.com/css2?family=Fira+Sans:wght@300;400;500&display=swap">
<style>
  :root {
    --backdrop: #8dd49a;
    --paper: #ffffff;
    --teal: #0e7373;
    --ink: #4a4f55;
    --ink-dark: #2f3337;
    --mist: #c3d2d4;
  }
  * { margin: 0; padding: 0; box-sizing: border-box; }
  html, body {
    width: 958px;
    height: 1200px;
    overflow: hidden;
    background: var(--backdrop);
    font-family: "Fira Sans", sans-serif;
  }
  .stage {
    position: relative;
    width: 958px;
    height: 1200px;
  }
  .card {
    position: absolute;
    top: 306px;
    width: 380px;
    height: 587px;
    overflow: hidden;
  }
  .card--front { left: 59px; background: var(--paper); }
  .card--back  { left: 519px; background: var(--teal); }

  /* front */
  .brand {
    position: absolute;
    left: 84px;
    top: 64px;
    display: flex;
    align-items: center;
    gap: 16px;
  }
  .brand__dot {
    width: 16px;
    height: 16px;
    border-radius: 50%;
    background: var(--teal);
    flex: none;
  }
  .brand__name {
    font-weight: 500;
    font-size: 21px;
    line-height: 28px;
    color: var(--ink);
  }
  .slogan {
    position: absolute;
    left: 116px;
    top: 115px;
    font-weight: 300;
    font-size: 20px;
    line-height: 29px;
    color: var(--ink);
  }
  .contact {
    position: absolute;
    left: 35px;
    top: 355px;
    font-weight: 300;
    font-size: 16.5px;
    line-height: 23.5px;
    color: var(--ink-dark);
  }
  .contact__name {
    font-weight: 500;
    color: var(--teal);
  }
  .contact__lines { margin-top: 17px; }
  .contact__label {
    display: inline-block;
    width: 56px;
  }

  /* back */
  .back-brand {
    position: absolute;
    left: 35px;
    top: 64px;
    display: flex;
    align-items: center;
    gap: 16px;
  }
  .back-brand__dot {
    width: 16px;
    height: 16px;
    border-radius: 50%;
    background: var(--paper);
    flex: none;
  }
  .back-brand__name {
    font-weight: 500;
    font-size: 21px;
    line-height: 28px;
    color: var(--paper);
  }
  .services {
    position: absolute;
    left: 35px;
    right: 30px;
    top: 355px;
    list-style: none;
    font-weight: 300;
    font-size: 16.5px;
    line-height: 23.5px;
    color: var(--paper);
  }
  .services__item + .services__item { margin-top: 17px; }
  .services__item::before {
    content: "";
    display: block;
    width: 28px;
    height: 3px;
    border-radius: 2px;
    background: var(--mist);
    margin-bottom: 8px;
  }
</style>
</head>
<body>
  <main class="stage">
    <section class="card card--front" aria-label="Visitenkarte Vorderseite">
      <div class="brand">
        <span class="brand__dot"></span>
        <span class="brand__name">Konrad Wallmuth</span>
      </div>
      <p class="slogan">Soziale Dienstleistungen,<br>Beratung &amp; Therapie</p>
      <div class="contact">
        <p class="contact__name">Konrad Wallmuth</p>
        <p>Dipl. Sozialpädagoge (FH)<br>systemischer Einzel-, Paar-<br>und Familientherapeut (VKTB)</p>
        <p class="contact__lines">
          <span class="contact__label">Mobil:</span>0176 / 4 829 31 57<br>
          <span class="contact__label">Mail:</span>konrad-wallmuth@rundpost.de
        </p>
      </div>
    </section>

    <section class="card card--back" aria-label="Visitenkarte Rückseite">
      <div class="back-brand">
        <span class="back-brand__dot"></span>
        <span class="back-brand__name">Konrad Wallmuth</span>
      </div>
      <ul class="services">
        <li class="services__item">systemische Beratung &amp; Therapie</li>
        <li class="services__item">ambulante Hilfen zur Erziehung,<br>intensive Familienberatung,<br>aufsuchende Familientherapie</li>
        <li class="services__item">soziale Projekte, Erwachsenenbildung,<br>Lehraufträge</li>
      </ul>
    </section>
  </main>
</body>
</html>
```